Dornick and Associates Business Card

A business card that can be templates for all employees using our newly created logo and information. We are looking for stylish however simplistic in nature, clean looks are better than over the top, however creativity will be appreciated if it has the right appeal. Note: If you feel a type of card (plastic, metalic, carbon, raised lettering, etc) helps your design please specify.
Target Market(s)
Investigation ETC
Industry/Entity Type
Private Investigator
Contact Information for Business Card
Len Dornick
President
5173 Wexbury Road
Larkmoor NX 16390-4412
Cell: 724-555-0193; Office: 724-555-0147
Email: lendornick@dornickassociates.example
Font styles to use
Requirements
Must have
- Website DornickAssociates.example
- Name, address, phone number ETC
- Use of current Logo and color pallets if applicable
- TM By logo, small

Nice to have
- Would like to see with and without a photo on the design

Should not have
- Redesign of logo, changing of colors

```html
<!DOCTYPE html>
<html lang="en">
<head>
<meta charset="utf-8">
<title>Dornick and Associates Business Cards</title>
<link rel="stylesheet" href="https://fonts.googleapis.com/css2?family=Tinos:ital,wght@0,400;0,700;1,400&display=swap">
<style>
  :root {
    --page: #ffffff;
    --card-light: #e7e7e7;
    --card-dark: #2a343e;
    --brand-orange: #e8492a;
    --band-orange: #f26522;
    --band-glow: #f9a23b;
    --web-orange: #f07d22;
    --text-light: #ffffff;
    --photo-dark: #141414;
    --photo-mid: #4a4f57;
  }
  * { box-sizing: border-box; margin: 0; padding: 0; }
  html, body {
    width: 1200px; height: 1000px; overflow: hidden;
    background: var(--page);
    font-family: "Tinos", "Times New Roman", serif;
  }
  .card {
    position: absolute;
    width: 724px; height: 423px;
    background: var(--card-light);
    overflow: hidden;
  }
  .card--front { left: 78px; top: 73px; }
  .card--back { left: 390px; top: 511px; }

  .band {
    position: absolute; left: 0; width: 100%; height: 23px;
    background: linear-gradient(to bottom, var(--band-orange) 0%, var(--band-glow) 50%, var(--band-orange) 100%);
  }
  .card--front .band { top: 211px; }
  .card--back .band { top: 317px; }

  .panel { position: absolute; left: 0; bottom: 0; width: 100%; background: var(--card-dark); }
  .card--front .panel { top: 234px; }
  .card--back .panel { top: 340px; }

  .brand { position: absolute; display: flex; align-items: center; color: var(--brand-orange); font-weight: 700; }
  .brand__mark { border-radius: 50%; background: var(--brand-orange); flex: none; }
  .brand__name { line-height: 1; white-space: nowrap; }
  .card--front .brand { left: 34px; top: 48px; gap: 22px; }
  .card--front .brand__mark { width: 80px; height: 80px; }
  .card--front .brand__name { font-size: 46px; }
  .card--back .brand { left: 40px; top: 84px; gap: 34px; }
  .card--back .brand__mark { width: 150px; height: 150px; }
  .card--back .brand__name { font-size: 70px; }

  .portrait {
    position: absolute; left: 569px; top: 35px; width: 119px; height: 145px;
    border-radius: 8px;
    background: radial-gradient(circle at 50% 55%, var(--photo-mid) 0%, var(--photo-dark) 70%);
  }

  .address, .contact {
    position: absolute; color: var(--text-light); font-size: 22px; line-height: 30px;
  }
  .address { left: 34px; top: 305px; }
  .contact { right: 35px; top: 270px; text-align: right; }
  .contact__name { font-weight: 700; }
  .contact__title { font-style: italic; }
  .contact__cell strong { font-weight: 700; }
  .contact__email { font-size: 20px; }

  .website {
    position: absolute; left: 0; width: 100%; top: 0; bottom: 0;
    display: flex; align-items: center; justify-content: center;
    color: var(--web-orange); font-size: 40px; white-space: nowrap;
  }
</style>
</head>
<body>
  <section class="card card--front">
    <div class="brand">
      <span class="brand__mark"></span>
      <span class="brand__name">Dornick<br>and Associates</span>
    </div>
    <div class="portrait" role="img" aria-label="Portrait photo of Len Dornick, President"></div>
    <div class="band"></div>
    <div class="panel"></div>
    <p class="address">5173 Wexbury Road<br>Larkmoor, NX 16390-4412<br>Office: 724-555-0147</p>
    <div class="contact">
      <p class="contact__name">Len Dornick</p>
      <p class="contact__title">President</p>
      <p class="contact__cell">Cell: <strong>724-555-0193</strong></p>
      <p class="contact__email">lendornick@dornickassociates.example</p>
    </div>
  </section>

  <section class="card card--back">
    <div class="brand">
      <span class="brand__mark"></span>
      <span class="brand__name">Dornick<br>and Associates</span>
    </div>
    <div class="band"></div>
    <div class="panel">
      <p class="website">www.DornickAssociates.example</p>
    </div>
  </section>
</body>
</html>
```